An innovative software company needs a business card!

We need a business card design for our new innovative software company. Please use the details for the business card provided in business card details section. We will use the business card paper like: https://www.plavex.com/us/products/nfc/business-cards-plus.html Our company name: kelvora We have already a logo and colors to use in business cards too ,

Target Market(s)

App & Sofware Development

Industry/Entity Type

Software

Contact Information for Business Card

Lukas Brenner, BSc.
Owner and Creative Superhero

Adress:
Tulpenweg 37/4/1809
A - 1100, Wien

Tel: +43 (0) 676 921 35 60
Email: lukas.brenner@kelvora.at
Web: www.kelvora.at

Requirements
Must have
• - Use our logo
Nice to have
• It would be nice to have a nice picture on the backside. (About apps, software, technicals or funy stuff) - Use our colors as in business card (optional)

```html
<!DOCTYPE html>
<html lang="en">
<head>
<meta charset="utf-8">
<title>kelvora – business card</title>
<link href="https://fonts.googleapis.com/css2?family=Source+Sans+3:wght@400;600;700&display=swap" rel="stylesheet">
<style>
  :root {
    --stage: #d6d7d9;
    --brand-blue: #1ea5d0;
    --brand-blue-deep: #2585b0;
    --brand-blue-soft: #3aa6cf;
    --card-white: #ffffff;
    --muted-grey: #a9abad;
  }
  * { box-sizing: border-box; margin: 0; padding: 0; }
  html, body {
    width: 1200px; height: 1200px; overflow: hidden;
    background: var(--stage);
    font-family: "Source Sans 3", sans-serif;
  }
  .canvas { position: relative; width: 1200px; height: 1200px; }

  .card {
    position: absolute; left: 239px; width: 721px;
    overflow: hidden;
  }

  /* Front side */
  .card--front { top: 163px; height: 413px; }
  .front-backdrop {
    position: absolute; inset: 0;
    background: linear-gradient(120deg, var(--brand-blue-deep) 0%, var(--brand-blue-soft) 55%, var(--brand-blue-deep) 100%);
  }
  .front-logo {
    position: absolute; left: 318px; top: 256px;
    display: flex; align-items: center; gap: 22px;
  }
  .front-logo .logo-dot {
    width: 64px; height: 64px; border-radius: 50%;
    background: var(--card-white);
  }
  .front-logo .logo-name {
    font-size: 76px; font-weight: 700; line-height: 1;
    color: var(--card-white); letter-spacing: -1px;
  }

  /* Back side */
  .card--back { top: 613px; height: 410px; background: var(--card-white); }
  .back-logo {
    position: absolute; left: 0; right: 0; top: 66px;
    display: flex; justify-content: center; align-items: center; gap: 20px;
  }
  .back-logo .logo-dot {
    width: 64px; height: 64px; border-radius: 50%;
    background: var(--brand-blue);
  }
  .back-logo .logo-name {
    font-size: 74px; font-weight: 700; line-height: 1;
    color: var(--brand-blue); letter-spacing: -1px;
  }
  .holder {
    position: absolute; left: 0; right: 0; top: 178px; text-align: center;
  }
  .holder-name {
    font-size: 29px; font-weight: 600; color: var(--brand-blue); line-height: 1.1;
  }
  .holder-role {
    margin-top: 4px;
    font-size: 19px; font-weight: 400; color: var(--muted-grey);
  }
  .holder-address {
    margin-top: 8px;
    font-size: 16px; font-weight: 400; color: var(--muted-grey);
  }

  .contact-rule {
    position: absolute; left: 0; right: 0; top: 332px; height: 3px;
    background: var(--brand-blue);
  }
  .contact-band {
    position: absolute; left: 0; right: 0; top: 340px; bottom: 0;
    background: var(--brand-blue);
  }
  .contact-item {
    position: absolute; top: 318px; width: 220px; margin-left: -110px;
    text-align: center;
  }
  .contact-item .icon {
    display: block; margin: 0 auto; width: 30px; height: 30px;
  }
  .contact-item .value {
    display: block; margin-top: 17px;
    font-size: 17px; color: var(--card-white); white-space: nowrap;
  }
  .contact-item--phone { left: 150px; }
  .contact-item--mail { left: 361px; }
  .contact-item--web { left: 572px; }
</style>
</head>
<body>
<div class="canvas">

  <section class="card card--front">
    <div class="front-backdrop" role="img" aria-label="Close-up photo of website source code on a screen, tinted blue"></div>
    <div class="front-logo">
      <span class="logo-dot"></span>
      <span class="logo-name">kelvora</span>
    </div>
  </section>

  <section class="card card--back">
    <div class="back-logo">
      <span class="logo-dot"></span>
      <span class="logo-name">kelvora</span>
    </div>

    <div class="holder">
      <p class="holder-name">LUKAS BRENNER, BSC.</p>
      <p class="holder-role">Owner and Creative Superhero</p>
      <p class="holder-address">Tulpenweg 37/4/1809 · A - 1100, Wien</p>
    </div>

    <div class="contact-rule"></div>
    <div class="contact-band"></div>

    <div class="contact-item contact-item--phone">
      <svg class="icon" viewBox="0 0 30 30" aria-hidden="true">
        <circle cx="15" cy="15" r="13" fill="var(--brand-blue)" stroke="#fff" stroke-width="2.5"/>
        <path d="M10.5 8.5c.8-.6 1.6-.4 2 .3l1.2 2.2c.4.7.2 1.3-.4 1.7l-.8.5c.7 1.7 1.9 3 3.5 3.8l.6-.8c.4-.6 1.1-.7 1.7-.3l2.1 1.3c.7.4.8 1.2.2 1.9-1 1.3-2.4 1.8-4 1.1-3.2-1.4-5.6-3.900-6.9-7.1-.6-1.6-.3-3.1.8-4.6z" fill="#fff"/>
      </svg>
      <span class="value">+43 (0) 676 921 35 60</span>
    </div>

    <div class="contact-item contact-item--mail">
      <svg class="icon" viewBox="0 0 30 30" aria-hidden="true">
        <circle cx="15" cy="15" r="13" fill="var(--brand-blue)" stroke="#fff" stroke-width="2.5"/>
        <rect x="8" y="10" width="14" height="10" rx="1" fill="#fff"/>
        <path d="M8.5 10.5l6.5 5 6.5-5" fill="none" stroke="var(--brand-blue)" stroke-width="1.3"/>
      </svg>
      <span class="value">lukas.brenner@kelvora.at</span>
    </div>

    <div class="contact-item contact-item--web">
      <svg class="icon" viewBox="0 0 30 30" aria-hidden="true">
        <circle cx="15" cy="15" r="13" fill="var(--brand-blue)" stroke="#fff" stroke-width="2.5"/>
        <circle cx="15" cy="15" r="7" fill="#fff"/>
        <path d="M8 15h14M15 8c-2.5 2.2-2.5 11.8 0 14M15 8c2.5 2.2 2.5 11.8 0 14" fill="none" stroke="var(--brand-blue)" stroke-width="1.1"/>
      </svg>
      <span class="value">www.kelvora.at</span>
    </div>
  </section>

</div>
</body>
</html>
```